Real Estate Web Design

Hi

We are a real estate agency who is looking for a Corporate Design that would match our Style Guide. We have already developed the website but we want to apply our Branding on top of it. I am looking for some creative concepts

Below is our Test link for our new website
http://brightkeyhomes.sampledemo.com.au/

Attached is our Style Guide

Cheers
Ruvo

Industry/Entity Type

Real Estate

```html
<!DOCTYPE html>
<html lang="en">
<head>
<meta charset="utf-8">
<title>Bright Key Homes</title>
<link rel="stylesheet" href="https://fonts.googleapis.com/css2?family=Open+Sans:wght@300;400;600;700&display=swap">
<style>
:root{
  --blue:#0b5aa8;
  --blue-dark:#064080;
  --blue-deep:#043a78;
  --red:#d3171b;
  --red-dark:#b30f12;
  --text:#444;
  --muted:#8a8a8a;
  --line:#e3e3e3;
  --white:#fff;
}
*{box-sizing:border-box;margin:0;padding:0}
html,body{width:1200px;height:2817px;overflow:hidden;background:var(--white)}
body{position:relative;font-family:"Open Sans",Arial,sans-serif;color:var(--text)}
.abs{position:absolute}
.site-header{left:0;top:0;width:1200px;height:124px}
.brand{left:79px;top:30px;display:flex;align-items:center;gap:14px}
.brand-mark{width:34px;height:34px;border-radius:50%;background:var(--red)}
.brand-name{font-size:36px;font-weight:700;color:var(--red);letter-spacing:-.5px}
.call{right:70px;top:40px;text-align:right;color:var(--blue)}
.call small{display:block;font-size:21px;font-weight:400}
.call strong{display:flex;align-items:center;gap:8px;font-size:31px;font-weight:400;color:var(--blue-dark)}
.main-nav{left:0;top:124px;width:1200px;height:54px;background:linear-gradient(#1a6dc0,var(--blue-dark));display:flex;padding-left:70px}
.main-nav a{color:#fff;text-decoration:none;font-size:18px;line-height:54px;padding:0 17px;border-right:1px solid rgba(255,255,255,.2)}
.main-nav a:first-child{padding-left:16px}
.hero{left:0;top:178px;width:1200px;height:457px;background:linear-gradient(135deg,#7a6a44,#b89264 40%,#8c6a44 70%,#5b4a2e)}
.hero-video{left:70px;top:90px;width:437px;height:280px;border:5px solid #fff;background:linear-gradient(#6e8fb8,#9c8e78 60%,#4e7a3a);box-shadow:0 2px 8px rgba(0,0,0,.4)}
.play{left:190px;top:110px;width:56px;height:56px;border-radius:50%;background:rgba(0,0,0,.75);border:3px solid #fff}
.play::after{content:"";position:absolute;left:20px;top:14px;border-left:18px solid #fff;border-top:11px solid transparent;border-bottom:11px solid transparent}
.search{left:804px;top:60px;width:329px;height:340px;background:var(--red);padding:20px 24px;color:#fff;font-size:13px;box-shadow:0 2px 8px rgba(0,0,0,.3)}
.search label{display:block;line-height:18px;margin-bottom:4px}
.field{height:32px;background:#fff;color:#999;font-size:12px;line-height:32px;padding-left:10px;margin-bottom:12px}
.pair{display:flex;gap:16px}.pair>div{flex:1}
.btn{position:absolute;right:22px;top:290px;background:var(--red-dark);border:1px solid #ff6a6a;color:#fff;font-size:14px;line-height:18px;padding:8px 16px}
.dots{left:565px;top:425px;display:flex;gap:8px}
.dots i{width:14px;height:14px;border-radius:50%;background:rgba(255,255,255,.6)}
.dots i:first-child{background:#fff}
.promo h3{font-weight:400;color:var(--blue-dark);font-size:24px;line-height:1.2;white-space:nowrap}
.promo .pic{margin-top:12px;height:142px}
.divider{left:66px;top:933px;width:1068px;height:1px;background:var(--line)}
.section-title{width:1200px;left:0;text-align:center;font-weight:300;font-size:35px;color:#333}
.intro{left:100px;top:1030px;width:1000px;text-align:center;font-size:13.5px;line-height:24px;color:var(--muted);white-space:nowrap}
.listing{width:517px;height:221px;border:1px solid var(--line);background:#fff}
.listing .pic{left:20px;top:20px;width:182px;height:137px}
.listing .info{left:222px;top:18px;width:285px}
.listing h4{font-weight:400;font-size:20px;color:var(--red);line-height:28px;white-space:nowrap}
.listing .rent{color:var(--blue);font-size:16px;margin:2px 0 6px}
.listing p{font-size:12.5px;color:var(--muted);line-height:20px}
.specs{left:0;bottom:0;width:100%;height:41px;background:linear-gradient(#1663b4,var(--blue-dark));display:flex}
.specs span{flex:1;color:#fff;font-size:13px;display:flex;align-items:center;justify-content:center;gap:8px;border-right:1px solid rgba(255,255,255,.3)}
.specs span:last-child{border:0}
.reviews{left:0;top:1634px;width:1200px;height:360px;background:linear-gradient(var(--red),#c31217 60%,#a80d10)}
.review{top:109px;width:516px;height:169px;background:#fff;border-radius:8px;padding:20px 26px;box-shadow:0 3px 8px rgba(0,0,0,.25)}
.review h5{font-weight:400;font-size:19px;color:#333}
.review .by{font-size:14px;color:var(--blue);margin:6px 0 14px}
.review .by b{color:var(--red);letter-spacing:2px;font-weight:400}
.review p{font-size:13px;color:var(--muted);line-height:21px}
.feature{top:2101px;width:256px;height:331px;border:1px solid var(--line);padding:12px}
.feature .pic{height:144px}
.feature h4{margin-top:16px;font-weight:400;font-size:16px;line-height:22px;color:#333}
.feature p{margin-top:6px;font-size:12px;line-height:19px;color:var(--muted)}
.feature a{display:block;margin-top:10px;font-size:12px;color:var(--blue);text-decoration:none}
.site-footer{left:0;top:2471px;width:1200px;height:346px;background:linear-gradient(var(--blue),var(--blue-deep) 70%,#0a4f98);color:#cfe0f5;font-size:14px;line-height:26px}
.site-footer h6{font-weight:400;font-size:24px;color:#fff;margin-bottom:10px}
.col{top:38px}
.col ul{list-style:none}
.contact p{font-size:13.5px;white-space:nowrap}
.social{display:flex;gap:8px;margin-top:12px}
.social i{width:28px;height:28px;border-radius:50%;background:#fff}
.copy{left:0;top:286px;width:1200px;border-top:1px solid rgba(255,255,255,.2);padding:16px 79px;font-size:12px;color:#9fbde0}
</style>
</head>
<body>
<header class="site-header abs">
  <div class="brand abs"><span class="brand-mark"></span><span class="brand-name">Bright Key Homes</span></div>
  <div class="call abs"><small>Call Us Now</small><strong><svg width="26" height="26" viewBox="0 0 24 24"><path fill="#064080" d="M6.6 10.8a15 15 0 0 0 6.6 6.6l2.2-2.2c.3-.3.7-.4 1-.2 1.1.4 2.3.6 3.6.6.6 0 1 .4 1 1V20c0 .6-.4 1-1 1A17 17 0 0 1 3 4c0-.6.4-1 1-1h3.5c.6 0 1 .4 1 1 0 1.3.2 2.5.6 3.6.1.3 0 .7-.2 1z"/></svg>08-5550-4172</strong></div>
</header>
<nav class="main-nav abs">
  <a>Home</a><a>About Us</a><a>Land lords</a><a>Tenants</a><a>Properties</a><a>Contact Us</a><a>Franchise Opportunities</a><a>Testimonials</a>
</nav>
<section class="hero abs" role="img" aria-label="Outdoor timber patio with garden and stone wall">
  <div class="hero-video abs" role="img" aria-label="Family seated in front of a brick home, video preview"><span class="play abs"></span></div>
  <form class="search abs">
    <label>Property Name</label><div class="field">Property type</div>
    <label>Zip Codes</label><div class="field"></div>
    <div class="pair"><div><label>Mini Price</label><div class="field">0</div></div><div><label>Max Price</label><div class="field">0</div></div></div>
    <div class="pair"><div><label>Bedrooms</label><div class="field">0</div></div><div><label>Bathrooms</label><div class="field">0</div></div></div>
    <span class="btn">LIST PROPERTIES</span>
  </form>
  <div class="dots abs"><i></i><i></i><i></i><i></i></div>
</section>
<div class="promo abs" style="left:70px;top:676px;width:324px"><h3>Do you want your<br>Property Managed?</h3><div class="pic" role="img" aria-label="Close-up of woven outdoor chair" style="background:linear-gradient(135deg,#5a2a10,#c8742e 50%,#7a3a14)"></div></div>
<div class="promo abs" style="left:438px;top:676px;width:326px"><h3>How much rent<br>can I get per week?</h3><div class="pic" role="img" aria-label="Smiling woman resting her chin on her hand" style="background:linear-gradient(90deg,#dfe6ec,#f1e4d6 50%,#b9cf9a);border:1px solid #ddd"></div></div>
<div class="promo abs" style="left:806px;top:676px;width:330px"><h3 style="color:var(--red);font-size:25px;margin-top:2px">Franchise Opportunities</h3><div class="pic" role="img" aria-label="Map of Australia with states marked" style="margin:22px 0 0 26px;width:210px;height:140px;background:linear-gradient(#f59a3c,#e8781c);border-radius:30px 50px 40px 20px"></div></div>
<div class="divider abs"></div>
<h2 class="section-title abs" style="top:978px">We are Offering the Best Real Estate Deals</h2>
<p class="intro abs">For the past 10 years in the South West we have been the leading specialist rental company. We have provided satisfaction to hundred's of land-<br>lords by getting the best tenant, paying the best rent in the shortest possible time.</p>

<article class="listing abs" style="left:68px;top:1117px"><div class="pic abs" role="img" aria-label="Tropical home with thatched roof and pool" style="background:linear-gradient(#4a86c8,#7a6a4a 55%,#3f7a3a)"></div><div class="info abs"><h4>8 Wren Road, Carey Park</h4><div class="rent">Rent : $ 270 / month</div><p>Comfortable 3 bedroom, 1 bathroom home with lounge and kitchen/dining area, as well as a sunken g...</p></div><div class="specs abs"><span>0 mtr sq</span><span>3 Bedrooms</span><span>1 Bedrooms</span></div></article>
<article class="listing abs" style="left:614px;top:1117px"><div class="pic abs" role="img" aria-label="Two-storey rendered house with garage" style="background:linear-gradient(#8fb0d4,#c9b08a 55%,#8a8a7a)"></div><div class="info abs"><h4>35 Marlowe Road,<br>AUSTRALIND WA 6233</h4><div class="rent">Rent : $ 270 / month</div><p>Newly built quality Harlow Build home with no expense spared and within a minutes</p></div><div class="specs abs"><span>0 mtr sq</span><span>3 Bedrooms</span><span>1 Bedrooms</span></div></article>
<article class="listing abs" style="left:68px;top:1367px"><div class="pic abs" role="img" aria-label="White weatherboard house on a lawn" style="background:linear-gradient(#a9c6e2,#e8e8e2 50%,#5f8a3e)"></div><div class="info abs"><h4>15 Tallis Crescent,<br>CAREY PARK WA 6230</h4><div class="rent">Rent : $ 270 / month</div><p>Renovated Internally,3 large Bedrooms 1 Bathroom newly appointed rooms</p></div><div class="specs abs"><span>0 mtr sq</span><span>3 Bedrooms</span><span>1 Bedrooms</span></div></article>
<article class="listing abs" style="left:614px;top:1367px"><div class="pic abs" role="img" aria-label="Apartment complex with palm trees and pool" style="background:linear-gradient(#5d94d0,#d9b78a 55%,#3a86b0)"></div><div class="info abs"><h4>2/41 Ward Street, Carey Park</h4><div class="rent">Rent : $ 270 / month</div><p>Comfortable 3 bedroom, 1 bathroom home with lounge and kitchen/dining area, as well as a sunken g...</p></div><div class="specs abs"><span>0 mtr sq</span><span>3 Bedrooms</span><span>1 Bedrooms</span></div></article>

<section class="reviews abs">
  <h2 class="section-title abs" style="top:43px;color:#fff">What our Customers think</h2>
  <div class="review abs" style="left:70px"><h5>The experience of finding a rental was e</h5><div class="by">by Nathan R. &nbsp;viareview <b>★★★★★</b></div><p>The experience of finding a rental was excellent and the staff were very professional and I couldn't have asked for more.</p></div>
  <div class="review abs" style="left:612px"><h5>Bright Key Homes have been manag</h5><div class="by">by Colin Ashdown &nbsp;viareview <b>★★★★★</b></div><p>Bright Key Homes have been managing my property for over two years and have always provided an excellent service. They consistently provide monthly statements, regular property inspection reports</p></div>
</section>

<h2 class="section-title abs" style="top:2040px">Featured Properties</h2>
<article class="feature abs" style="left:70px"><div class="pic" role="img" aria-label="Family home with large shed" style="background:linear-gradient(#7aa6d6,#d8d4c8 55%,#6a8a4a)"></div><h4>Family home in Ridgeview with Large Shed</h4><p>This comfortable family home with a large shed/workshop is well positioned close to shopping centres....</p><a>Learn More ›</a></article>
<article class="feature abs" style="left:340px"><div class="pic" role="img" aria-label="Brick house with double garage" style="background:linear-gradient(#9cbcdc,#b88a6a 55%,#6e7a5a)"></div><h4>18 Kestrel Turn, Dalyellup</h4><p>Quiet street close to parks and schools. Large living areas, modern kitchen, two bathrooms, lock up garage.</p><a>Learn More ›</a></article>
<article class="feature abs" style="left:608px"><div class="pic" role="img" aria-label="Apartment terrace at dusk beside a pool" style="background:linear-gradient(#e8a070,#7a5a44 55%,#3a6a8a)"></div><h4>unit 7/18 Harbourline Blvd Bunbury</h4><p>Spacious, stylishly furnished apartment in prime bunbury location with award winning restaurants and...</p><a>Learn More ›</a></article>
<article class="feature abs" style="left:877px"><div class="pic" role="img" aria-label="Row of two-storey townhouses" style="background:linear-gradient(#7aa0c8,#8a9a7a 55%,#5a6a4a)"></div><h4>48 Pennell Close, Australind</h4><p>Neat family home near the river, open plan living, shaded patio, ducted cooling and secure rear yard.</p><a>Learn More ›</a></article>

<footer class="site-footer abs">
  <div class="col abs" style="left:79px;width:320px"><h6>About Bright Key Homes</h6><p>You'll find just what you need with Bright Key Homes. Not only do we offer a completely unparalleled range of properties and locations, we're also the first choice for property owners looking for a singularly dedicated property management specialist. More...</p></div>
  <div class="col abs" style="left:451px"><h6>Quick Links</h6><ul><li>Frequently asked Questions</li><li>How do I pay rent?</li><li>Tenant Policies</li><li>Tenants Information</li></ul></div>
  <div class="col abs" style="left:691px"><h6>Quick Links</h6><ul><li>Newsletter</li><li>Legal Information</li><li>Sitemap</li></ul></div>
  <div class="col contact abs" style="left:886px"><h6>Contact Info</h6><p><b style="color:#fff;font-weight:600">First Floor</b><br>27 Calloway Street<br>Bunbury WA 6230<br>Phone no. 08-5550-4172<br>Email address: info@brightkeyhomes.com.au</p><div class="social"><i></i><i></i><i></i><i></i></div></div>
  <div class="copy abs">© 2013 Company Name. All right reserved. Term of Use</div>
</footer>
</body>
</html>
```